Business and Success Coaching Business Card

Need a business card for my coaching business. I coach small businesses, career professionals and, individuals wanting to unlock their human potential and achieve excellence. At the heart of our methodology is the Shaping Purposeful Action Routines Knowingly (SPARK) approach to formulate empowerment, create principles for success and setting achievable outcomes. I would like something that incorporates our new logo, something clean and sharp with a solid darker, but complementary background, color on the card front. The back should be white where there will be room for three questions

Target Market(s)

People looking to advance and improve themselves through a success coach

Industry/Entity Type

Life Coaching

Contact Information for Business Card

Contact information on card.
Business name on front of card
Questions on back

Font styles to use
Other font styles liked:
• Century Gothic or other Serif style fonts that look similar to Century Gothic

Colors

Designer to choose colors to be used in the design.

Requirements
Must have
• Logo on front of card
• Business name - The Steady Forge
• Contact name - Ted Harlow
• Address - Box 4619, Ridgeview, CO 80127-4619
• Phone number - 303-555-0147
• Email address - harlow.ted@thesteadyforge.example
• Certifications - CPC, CMHt, PCT, MNLP
• Back of card
• Three questions on the back of the card:
• If you were at your best, what would you do right now?
• What is the decision you have been avoiding?
• What's one action you could take in the next 10 minutes?
Nice to have
• I would like to see a solid color on the front of the card that compliments the logo.
• Back should be white, or could be contrasting, but need to have the three questions.

```html
<!DOCTYPE html>
<html lang="en">
<head>
<meta charset="utf-8">
<title>The Steady Forge – Business Card</title>
<link rel="stylesheet" href="https://fonts.googleapis.com/css2?family=Questrial&family=Mulish:wght@400;700;800&display=swap">
<style>
  :root {
    --stage: #2a2a2c;
    --navy-deep: #0d1630;
    --navy: #18244a;
    --brand-blue: #2d4f98;
    --sky: #4a86d0;
    --ink: #1d3470;
    --paper: #ffffff;
    --soft-text: #c9cfdc;
    --rule: #b9c0cf;
  }
  * { box-sizing: border-box; margin: 0; padding: 0; }
  html, body { width: 1200px; height: 1200px; overflow: hidden; }
  body {
    background: var(--stage);
    display: flex;
    flex-direction: column;
    align-items: center;
    justify-content: center;
    gap: 56px;
    font-family: "Questrial", "Century Gothic", sans-serif;
  }
  .card {
    position: relative;
    width: 860px;
    height: 491px;
    overflow: hidden;
    box-shadow: 0 14px 40px rgba(0,0,0,.45);
  }

  /* Back */
  .card-back { background: var(--paper); }
  .questions {
    position: absolute;
    top: 150px; left: 0; right: 0;
    text-align: center;
    font-family: "Mulish", "Century Gothic", sans-serif;
    font-weight: 800;
    font-size: 22px;
    line-height: 1.45;
    color: var(--ink);
    list-style: none;
    letter-spacing: .3px;
  }
  .web-band {
    position: absolute;
    left: 0; right: 0; bottom: 0;
    height: 44px;
    background: var(--sky);
    color: var(--paper);
    display: flex; align-items: center; justify-content: center;
    font-size: 17px;
    letter-spacing: 14px;
    text-transform: uppercase;
  }

  /* Front */
  .card-front {
    background: linear-gradient(135deg, var(--navy-deep) 0%, var(--navy) 100%);
    color: var(--soft-text);
  }
  .brand {
    position: absolute;
    left: 56px; top: 130px;
  }
  .brand-name {
    font-family: "Mulish", "Century Gothic", sans-serif;
    font-weight: 800;
    font-size: 42px;
    color: var(--brand-blue);
    display: flex; align-items: center; gap: 14px;
  }
  .brand-dot {
    width: 20px; height: 20px; border-radius: 50%;
    background: var(--brand-blue);
  }
  .brand-tagline {
    font-size: 22px;
    margin-top: 2px;
    padding-left: 54px;
    color: var(--soft-text);
  }
  .person {
    position: absolute;
    right: 0; top: 150px;
    text-align: right;
  }
  .person-name {
    font-family: "Mulish", "Century Gothic", sans-serif;
    font-weight: 800;
    font-size: 27px;
    color: var(--paper);
    letter-spacing: 1px;
    padding-right: 60px;
    text-transform: uppercase;
  }
  .credentials {
    margin-top: 4px;
    background: var(--sky);
    color: var(--paper);
    font-size: 21px;
    letter-spacing: 1px;
    padding: 3px 60px 3px 16px;
    display: inline-block;
  }
  .divider {
    position: absolute;
    left: 56px; right: 56px; top: 272px;
    border-top: 1px solid var(--rule);
  }
  .contacts {
    position: absolute;
    left: 56px; top: 300px;
    list-style: none;
    font-size: 19px;
    line-height: 1.5;
    color: var(--soft-text);
  }
  .contacts li { display: flex; align-items: center; gap: 12px; }
  .contacts svg { width: 18px; height: 18px; fill: var(--sky); flex: none; }
  .address {
    position: absolute;
    right: 60px; top: 318px;
    text-align: right;
    font-size: 20px;
    font-style: normal;
    line-height: 1.4;
    color: var(--soft-text);
  }
  .base-bands {
    position: absolute; left: 0; bottom: 0;
    width: 860px; height: 70px;
  }
</style>
</head>
<body>

  <section class="card card-back" aria-label="Card back">
    <ul class="questions">
      <li>If you were at your best, what would you do right now?</li>
      <li>What is the decision you have been avoiding?</li>
      <li>What's one action you could take in the next 10 minutes?</li>
    </ul>
    <div class="web-band">www.thesteadyforge.example</div>
  </section>

  <section class="card card-front" aria-label="Card front">
    <div class="brand">
      <div class="brand-name"><span class="brand-dot"></span>The Steady Forge</div>
      <div class="brand-tagline">Power up your next chapter</div>
    </div>

    <div class="person">
      <div class="person-name">Ted Harlow</div>
      <div class="credentials">CPC, CMHt, PCT, MNLP</div>
    </div>

    <div class="divider"></div>

    <ul class="contacts">
      <li>
        <svg viewBox="0 0 24 24" aria-hidden="true"><path d="M6.6 10.8a15.1 15.1 0 0 0 6.6 6.6l2.2-2.2a1 1 0 0 1 1-.25 11.4 11.4 0 0 0 3.6.57 1 1 0 0 1 1 1V20a1 1 0 0 1-1 1A17 17 0 0 1 3 4a1 1 0 0 1 1-1h3.5a1 1 0 0 1 1 1c0 1.25.2 2.45.57 3.570a1 1 0 0 1-.25 1z"/></svg>
        303-555-0147
      </li>
      <li>
        <svg viewBox="0 0 24 24" aria-hidden="true"><path d="M2 5h20v14H2zm2 2v.4l8 5 8-5V7zm0 2.8V17h16V9.8l-8 5z"/></svg>
        harlow.ted@thesteadyforge.example
      </li>
      <li>
        <svg viewBox="0 0 24 24" aria-hidden="true"><path d="M12 2a10 10 0 1 0 0 20 10 10 0 0 0 0-20zm6.9 9h-3a15 15 0 0 0-1.3-5.6A8 8 0 0 1 18.9 11zM12 4.1c.9 1.2 1.8 3.5 1.9 6.9h-3.8c.1-3.4 1-5.7 1.9-6.9zM9.4 5.4A15 15 0 0 0 8.1 11h-3a8 8 0 0 1 4.3-5.6zM5.1 13h3a15 15 0 0 0 1.3 5.6A8 8 0 0 1 5.1 13zm6.9 6.9c-.9-1.2-1.8-3.5-1.9-6.9h3.8c-.1 3.4-1 5.7-1.9 6.9zm2.6-1.3a15 15 0 0 0 1.3-5.6h3a8 8 0 0 1-4.3 5.6z"/></svg>
        www.thesteadyforge.example
      </li>
    </ul>

    <address class="address">
      Box 4619, Ridgeview<br>CO 80127-4619
    </address>

    <svg class="base-bands" viewBox="0 0 860 70" aria-hidden="true">
      <polygon points="0,8 700,58 690,64 0,20" fill="var(--sky)"/>
      <polygon points="0,24 690,66 720,52 860,58 860,70 0,70" fill="#2c4da8"/>
    </svg>
  </section>

</body>
</html>
```